Real Estate - Large Sign Design

I am looking for a fresh new look for our leasing signs that will be showcase in front of commercial buildings available for lease. The sign dimension can be either 8'x4' or 4'x8'. They must exemplify our brand (see attachments) and be very visible by people driving by at high speeds.
They must include the following:
- Our logo (vector attached)
- Office Space Available
- 482-917-3064
- Mara Finch
- Peter Vale
- www.lorvanix.com
Please let me know if you have any questions.
Target Market(s)
Drivers in high traffic areas, walking crowds
Industry/Entity Type
Real Estate
Requirements
Must have
- They must include the following:
- - Our logo (vector attached)
- - Office Space Available
- - 482-917-3064
- - Mara Finch
- - Peter Vale
- - www.lorvanix.com
Should not have
- Should not be busy or hard to read.

```html
<!DOCTYPE html>
<html lang="en">
<head>
<meta charset="utf-8">
<title>Office Space Available – Leasing Sign</title>
<link rel="stylesheet" href="https://fonts.googleapis.com/css2?family=Open+Sans:wght@400;700;800&display=swap">
<style>
  :root {
    --charcoal: #3e3e40;
    --leaf: #7ac143;
    --green-bright: #0ea14f;
    --green-soft-start: #67ad5b;
    --green-soft-end: #1e9c5c;
    --green-deep-start: #2f7d4c;
    --green-deep-end: #1a3a2e;
    --white: #ffffff;
  }
  html, body {
    margin: 0;
    padding: 0;
    width: 1200px;
    height: 594px;
    overflow: hidden;
    background: var(--charcoal);
  }
  .sign {
    position: relative;
    width: 1200px;
    height: 594px;
    overflow: hidden;
    font-family: "Open Sans", Arial, sans-serif;
    background: var(--charcoal);
  }
  .sign__backdrop {
    position: absolute;
    inset: 0;
    width: 1200px;
    height: 594px;
  }
  .brand {
    position: absolute;
    left: 893px;
    top: 32px;
    margin: 0;
    color: var(--white);
    font-weight: 700;
    font-size: 46px;
    line-height: 52px;
    letter-spacing: 0.01em;
  }
  .brand span { display: block; }
  .offer {
    position: absolute;
    left: 0;
    top: 230px;
    width: 858px;
    text-align: center;
  }
  .offer__headline {
    margin: 0;
    color: var(--leaf);
    font-weight: 800;
    font-size: 94px;
    line-height: 96px;
    letter-spacing: 0.005em;
  }
  .offer__status {
    margin: 0;
    color: var(--leaf);
    font-weight: 800;
    font-size: 48px;
    line-height: 52px;
    letter-spacing: 0.6em;
    padding-left: 0.6em;
  }
  .contact {
    position: absolute;
    left: 0;
    top: 404px;
    width: 858px;
    text-align: center;
    color: var(--white);
  }
  .contact p { margin: 0; }
  .contact__names,
  .contact__phone {
    font-weight: 700;
    font-size: 44px;
    line-height: 54px;
  }
  .contact__web {
    font-weight: 400;
    font-size: 44px;
    line-height: 54px;
  }
</style>
</head>
<body>
  <main class="sign">
    <svg class="sign__backdrop" viewBox="0 0 1200 594" aria-hidden="true">
      <defs>
        <linearGradient id="band-soft" x1="0" y1="0" x2="1" y2="0.3">
          <stop offset="0" stop-color="var(--green-soft-start)"/>
          <stop offset="1" stop-color="var(--green-soft-end)"/>
        </linearGradient>
        <linearGradient id="band-deep" x1="0" y1="0" x2="0.4" y2="1">
          <stop offset="0" stop-color="var(--green-deep-start)"/>
          <stop offset="1" stop-color="var(--green-deep-end)"/>
        </linearGradient>
      </defs>
      <rect class="field" width="1200" height="594" fill="var(--charcoal)"/>
      <polygon class="band-soft" points="0,0 726,0 836,230 0,105" fill="url(#band-soft)"/>
      <polygon class="band-bright" points="726,0 1200,0 1200,286 832,230" fill="var(--green-bright)"/>
      <polygon class="band-deep" points="832,230 1200,286 1200,594 1005,594" fill="url(#band-deep)"/>
    </svg>

    <p class="brand"><span>Halvern</span><span>Estate</span><span>Group</span></p>

    <section class="offer">
      <h1 class="offer__headline">OFFICE SPACE</h1>
      <p class="offer__status">AVAILABLE</p>
    </section>

    <section class="contact">
      <p class="contact__names">Mara Finch &amp; Peter Vale</p>
      <p class="contact__phone">482-917-3064</p>
      <p class="contact__web">www.lorvanix.com</p>
    </section>
  </main>
</body>
</html>
```